Banner Ads, Icons, Logos, Photos for Chamber of Commerce

We just joined a chamber of commerce. I need several items made up with our logo and branding. We do not have a copy of our logo in large format. All logo and colors can be found on our website: http://www.myridgelinerails.example

2 Banner ads – 480 pixels w x 60 pixels h and 72 dpi in jpg or png
1 Homepage ad – 600 pixels w x 100 pixels h and 72 dpi in jpg or png
1 Search Results Icon max size is 75 x 75 pixels 72 dpi in jpg or png
1 Logo max size is 150 pixels w x 100 pixels h 72 dpi in jpg or png
1 Member Page photos max size is 600 x 600 pixels 72 dpi in jpg or png.
1 Thumbnail size is 150 x 150 pixels.

Industry/Entity Type

Residential Construction

Font styles to use
Sans Serif

Colors
0392cd
34a6d7
85cae6
cfe9f4
fbf289
fbee3d
cfdeed
85acd3

Requirements
Must have
• Logo
• phone number ( 555-316-2047 )
• "Free Estimates"
Nice to have
• Fence Photos - 1 wood fence photo, 1 aluminum fence photo, 1 vinyl fence photo
Should not have
• Too many words, too many colors

```html
<!DOCTYPE html>
<html lang="en">
<head>
<meta charset="utf-8">
<title>Ridgeline Rails – Chamber Banners</title>
<link href="https://fonts.googleapis.com/css2?family=Exo+2:wght@500;600&family=Arimo:ital,wght@0,400;1,700&display=swap" rel="stylesheet">
<style>
  :root {
    --stage: #eeeeee;
    --paper: #ffffff;
    --brand-blue: #3d8fd6;
    --swoosh-blue: #0392cd;
    --swoosh-blue-light: #34a6d7;
    --swoosh-yellow: #fbf289;
    --ink: #1b1b1b;
    --photo-lawn: #4f7a3a;
    --photo-house: #c9cfc4;
    --photo-wood: #a8814f;
    --photo-vinyl: #b7c9a2;
  }
  html, body {
    margin: 0;
    width: 1200px;
    height: 900px;
    overflow: hidden;
    background: var(--stage);
  }
  .canvas {
    position: relative;
    width: 1200px;
    height: 900px;
  }
  .banner {
    position: absolute;
    display: block;
    background: var(--paper);
    box-shadow: 0 4px 6px rgba(0,0,0,0.35);
  }
  .banner--wide { left: 127px; top: 230px; width: 968px; height: 160px; }
  .banner--home { left: 130px; top: 455px; width: 1070px; height: 315px; }
  .brand-name { font-family: "Exo 2", sans-serif; font-weight: 600; fill: var(--brand-blue); }
  .brand-phone { font-family: "Exo 2", sans-serif; font-weight: 600; fill: var(--ink); }
  .brand-tagline { font-family: "Arimo", sans-serif; font-weight: 400; fill: var(--ink); }
  .offer { font-family: "Arimo", sans-serif; font-style: italic; font-weight: 700; fill: var(--paper); }
</style>
</head>
<body>
<main class="canvas">

  <svg class="banner banner--wide" viewBox="0 0 968 160" aria-label="Ridgeline Rails wide banner">
    <defs>
      <linearGradient id="lawn-a" x1="0" y1="0" x2="0" y2="1">
        <stop offset="0" stop-color="#dfe4dc"/>
        <stop offset="0.45" stop-color="var(--photo-house)"/>
        <stop offset="0.6" stop-color="#5e8a45"/>
        <stop offset="1" stop-color="var(--photo-lawn)"/>
      </linearGradient>
      <linearGradient id="wood-a" x1="0" y1="0" x2="1" y2="0">
        <stop offset="0" stop-color="#7b5a33"/>
        <stop offset="1" stop-color="var(--photo-wood)"/>
      </linearGradient>
      <linearGradient id="vinyl-a" x1="0" y1="0" x2="0" y2="1">
        <stop offset="0" stop-color="#6f8f3e"/>
        <stop offset="0.5" stop-color="var(--photo-vinyl)"/>
        <stop offset="1" stop-color="#3f5e2a"/>
      </linearGradient>
    </defs>
    <path role="img" aria-label="Photo: black aluminum fence in front of a white house" d="M330 0 H545 V160 H196 C268 118 310 62 330 0 Z" fill="url(#lawn-a)"/>
    <rect role="img" aria-label="Photo: wooden picket fence along a lawn" x="550" y="0" width="176" height="160" fill="url(#wood-a)"/>
    <rect role="img" aria-label="Photo: white vinyl fence with shrubs" x="730" y="0" width="238" height="160" fill="url(#vinyl-a)"/>
    <path class="swoosh swoosh--blue" d="M308 48 C285 110 225 150 100 160 H225 C275 135 300 95 322 38 Z" fill="var(--swoosh-blue-light)"/>
    <path class="swoosh swoosh--yellow" d="M330 0 H356 C332 70 290 128 226 160 H196 C268 118 310 62 330 0 Z" fill="var(--swoosh-yellow)"/>
    <text class="brand-name" x="96" y="55" font-size="19">Ridgeline Rails</text>
    <text class="brand-phone" x="96" y="77" font-size="19.5">555-316-2047</text>
    <text class="brand-tagline" x="96" y="92" font-size="7">"Because Good Fences Make Good Neighbors"</text>
    <text class="offer" x="310" y="141" font-size="22">"Free Estimates"</text>
  </svg>

  <svg class="banner banner--home" viewBox="0 0 1070 315" aria-label="Ridgeline Rails homepage banner">
    <defs>
      <linearGradient id="lawn-b" x1="0" y1="0" x2="0" y2="1">
        <stop offset="0" stop-color="#e4e7e2"/>
        <stop offset="0.4" stop-color="var(--photo-house)"/>
        <stop offset="0.55" stop-color="#6a9450"/>
        <stop offset="1" stop-color="var(--photo-lawn)"/>
      </linearGradient>
    </defs>
    <path role="img" aria-label="Photo: black aluminum fence in front of a white house and green lawn" d="M660 0 H1070 V315 H418 C560 240 638 130 660 0 Z" fill="url(#lawn-b)"/>
    <path class="swoosh swoosh--blue" d="M598 105 C560 215 450 288 190 315 H420 C525 268 588 190 615 95 Z" fill="var(--swoosh-blue)"/>
    <path class="swoosh swoosh--yellow" d="M660 0 H810 C762 150 650 262 512 315 H418 C560 240 638 130 660 0 Z" fill="var(--swoosh-yellow)"/>
    <text class="brand-name" x="190" y="108" font-size="38">Ridgeline Rails</text>
    <text class="brand-phone" x="190" y="152" font-size="36">555-316-2047</text>
    <text class="brand-tagline" x="190" y="180" font-size="12">"Because Good Fences Make Good Neighbors"</text>
    <text class="offer" x="605" y="279" font-size="46">"Free Estimates"</text>
  </svg>

</main>
</body>
</html>
```